Book cover: Stormy Days Survival for Kids (A5)

I have a book called Stormy Days Survival for Teens. It is a book for teenagers which gives them tips and tactics on how to survive life's challenges regarding friends, family, feelings, relationships and hard stuff in life generally. I will upload the cover of this book but you can see it on my past jobs as one of the designers her eon Pixel Bazaar did it for me.
I have a new book I've written called Stormy Days Survival for Kids. This is a parallel book to Stormy Days Survival for Teens, but it is specifically for 8 to 12 or 13 year olds, rather than for older teens.
A very important aspect of this job is that it SHOULD MATCH in some strong way - the Stormy Days Survival for Teens book. I will be selling them together, displaying them together and I want them to look like two of a pair. It might be that you use the same image as the first book but change the colour of the image so that it is bright orange and green perhaps? Or that there is another image but in the image is placed in the exact same position across the book as the first book. It needs to look like the books are by the same author.
However, I would like this one to look a bit "younger", more kid friendly. For example, a font that looks like it is for kids, or kids' writing perhaps.
I dont want to have photos on the book, and I dont think I want cartoons or drawings - because I'm not sure how this will tie in with the first book.
I want it to look modern, fresh and designed specifically for kids. The text needs to be:
Stormy Days Survival - For Kids!
Tips and ideas for 8 to 13 year olds about how to stay cool, calm and confident on even the toughest days!
The back cover is going to mostly just have the table of contents listed and a blurb, with one or two cartoons which I will supply. I am keen to pick a designer to just do the front cover first and will ask them to do the back cover later.
UPDATED: I have attached three files with fonts that I like.

```html
<!DOCTYPE html>
<html lang="en">
<head>
<meta charset="utf-8">
<title>Stormy Days Survival for Kids – Front Cover</title>
<link rel="stylesheet" href="https://fonts.googleapis.com/css2?family=Londrina+Outline&family=Permanent+Marker&display=swap">
<style>
  :root {
    --paper: #ffffff;
    --ink: #111111;
    --sunny: #f5f200;
    --toast-light: #d9a35f;
    --toast-dark: #9a5a26;
  }
  * { margin: 0; padding: 0; box-sizing: border-box; }
  html, body {
    width: 800px;
    height: 1200px;
    overflow: hidden;
    background: var(--paper);
  }
  .cover {
    position: relative;
    width: 800px;
    height: 1200px;
    background: var(--paper);
    color: var(--ink);
    overflow: hidden;
  }
  .feature-band {
    position: absolute;
    left: 0;
    top: 389px;
    width: 800px;
    height: 525px;
    background:
      radial-gradient(ellipse 230px 170px at 340px 260px, var(--toast-light) 0%, var(--toast-dark) 55%, rgba(245,242,0,0) 100%),
      var(--sunny);
  }
  .title {
    position: absolute;
    left: 0;
    top: 0;
    width: 800px;
    font-family: "Londrina Outline", "Comic Sans MS", cursive;
    color: var(--ink);
    line-height: 1;
    z-index: 2;
  }
  .title-line { position: absolute; white-space: nowrap; }
  .title-top {
    left: 148px;
    top: 78px;
    font-size: 72px;
  }
  .title-main {
    left: 172px;
    top: 140px;
    font-size: 200px;
    letter-spacing: 2px;
  }
  .title-tail {
    left: 330px;
    top: 318px;
    font-size: 118px;
  }
  .tagline {
    position: absolute;
    left: 107px;
    top: 942px;
    width: 620px;
    font-family: Helvetica, Arial, sans-serif;
    font-size: 20.5px;
    line-height: 1.3;
    color: var(--ink);
  }
  .author {
    position: absolute;
    right: 42px;
    top: 1040px;
    text-align: center;
  }
  .author-name {
    font-family: "Permanent Marker", "Arial Black", sans-serif;
    font-size: 36px;
    letter-spacing: 1px;
    text-transform: uppercase;
    line-height: 1.1;
  }
  .author-role {
    font-family: Helvetica, Arial, sans-serif;
    font-size: 23px;
    line-height: 1.2;
  }
</style>
</head>
<body>
  <main class="cover">
    <div class="feature-band" role="img" aria-label="Photo of a stack of toasted bread slices on a bright yellow background"></div>

    <h1 class="title">
      <span class="title-line title-top">stormy days</span>
      <span class="title-line title-main">Survival</span>
      <span class="title-line title-tail">for Kids</span>
    </h1>

    <p class="tagline">Tips and ideas for 8 to 13 year olds&nbsp; about how to stay cool, calm and confident on even the toughest days!</p>

    <div class="author">
      <p class="author-name">Marlee Thornton</p>
      <p class="author-role">clinical psychologist</p>
    </div>
  </main>
</body>
</html>
```